Power Point CI

Creat a Slide Master which we can use and also add new slides with bullets, or other graphic design which we can fill. Power Point Master Format - also amend the graphics on the PPT - especially the project roadmap or profile page. have a look on our website www.talvoreksa.io. I would also appreciate other slides which we can use and fill

Target Market(s)

companies - PE, HR Executive

Industry/Entity Type

Executive Search

Font styles to use
Serif
Other font styles liked:
• Calibri or Coast like on our website

Colors
0094D4
00A9DD
6FCCEA
C7EBF8
E9F6FB

Requirements
Must have
• needs to sleek and slim - prefer white and bright elegant Backgrounds
Nice to have
• it should somehow fit to our website and corporate CI
Should not have
• Full green CI

```html
<!DOCTYPE html>
<html lang="en">
<head>
<meta charset="utf-8">
<title>Talvoreksa – Slide Master</title>
<link href="https://fonts.googleapis.com/css2?family=Fira+Sans:wght@400;600;700&family=Open+Sans:wght@400;600;700&family=Cormorant+Garamond:wght@300;400&display=swap" rel="stylesheet">
<style>
:root{
  --page:#d9d8da;
  --teal:#135f78;
  --teal-dark:#0c4b60;
  --teal-text:#17627c;
  --sky:#6fcce9;
  --ice:#c7ebf8;
  --mist:#e9f6fb;
  --grey-row:#ececec;
  --grey-bar:#8e8e8e;
  --ink:#4a4a4a;
  --accent:#e3412f;
  --white:#ffffff;
}
*{box-sizing:border-box;margin:0;padding:0}
html,body{width:1200px;height:3104px;overflow:hidden;background:var(--page)}
body{position:relative;font-family:"Open Sans",sans-serif;color:var(--ink)}
.slide{position:absolute;width:540px;height:304px;background:var(--white);overflow:hidden}
.abs{position:absolute}
.hero-wrap{position:absolute;left:160px;top:82px;width:880px;height:496px;overflow:hidden}
.hero-wrap .slide{position:absolute;left:0;top:0;transform:scale(1.6296);transform-origin:0 0}
.teal-bg{position:absolute;left:0;top:0;width:540px;height:272px;background:linear-gradient(125deg,var(--teal) 0%,#16698a 45%,var(--teal-dark) 100%)}
.teal-full{height:304px}
.art-area{position:absolute;left:0;top:0;width:270px;height:272px;background:radial-gradient(ellipse at 45% 45%,rgba(199,235,248,.42) 0%,rgba(111,204,233,.18) 45%,rgba(111,204,233,0) 75%)}
.cities{position:absolute;left:0;bottom:0;width:540px;height:32px;display:flex;align-items:center;justify-content:center;font-family:"Fira Sans",sans-serif;font-size:8.5px;letter-spacing:1.2px;color:var(--teal-text)}
.h-title{font-family:"Fira Sans",sans-serif;font-weight:700;color:var(--white);font-size:25px;line-height:1.15}
.lead{color:var(--white);font-size:7.4px;line-height:1.25}
.date{color:var(--white);font-size:6px}
.brand{font-family:"Cormorant Garamond",serif;font-weight:300;color:var(--white);letter-spacing:3px;display:flex;align-items:center;gap:8px}
.brand-dot{display:inline-block;border-radius:50%;background:var(--ice)}
.footer-bar{position:absolute;left:14px;top:272px;width:516px;height:13px;background:var(--teal);border-radius:7px;display:flex;align-items:center;justify-content:flex-end;padding-right:12px;color:var(--white);font-size:5px;gap:10px}
.footer-bar .num{border-left:1px solid rgba(255,255,255,.5);padding-left:8px;font-size:5.5px}
.footer-brand{position:absolute;left:20px;top:257px;display:flex;align-items:center;gap:4px;font-family:"Open Sans",sans-serif;font-weight:600;font-size:8px;color:var(--teal-text)}
.footer-brand i{width:7px;height:7px;border-radius:50%;background:var(--sky)}
.s-title{position:absolute;left:0;width:540px;text-align:center;font-family:"Fira Sans",sans-serif;font-weight:600;font-size:14.5px;color:var(--teal-text)}
.name{font-family:"Fira Sans",sans-serif;font-weight:600;font-size:19px;line-height:1.05;color:var(--teal-text)}
.bio{font-size:6.3px;line-height:1.18;color:var(--ink)}
.bio p{margin-bottom:5px}
.photo{position:absolute;background:linear-gradient(160deg,#6d6d6d,#2a2a2a 70%,#1a1a1a)}
.bullets{font-size:6.3px;line-height:1.2;padding-left:10px}
.bullets li{margin-bottom:5px}
.values{position:absolute;left:0;top:98px;width:540px;display:flex;justify-content:space-around}
.value{width:100px;text-align:center}
.value .ic{width:34px;height:34px;border-radius:50%;background:var(--teal);margin:0 auto 8px;display:flex;align-items:center;justify-content:center}
.value h4{font-family:"Fira Sans",sans-serif;font-size:8px;color:var(--teal-text);margin-bottom:7px}
.value p{font-size:5.7px;line-height:1.2;color:#777}
.ref{position:absolute;width:230px}
.ref h4{font-family:"Fira Sans",sans-serif;font-size:8.5px;color:var(--teal-text);margin-bottom:12px}
.ref .row{display:flex;height:23px;align-items:center;font-size:6px}
.ref .row:nth-child(odd){background:var(--grey-row)}
.ref .row b{width:115px;padding-left:4px;color:var(--teal-text);font-weight:700}
.proc-band{position:absolute;left:0;top:75px;width:540px;height:19px;background:var(--teal-dark);display:flex;color:var(--white);font-size:5.8px}
.proc-band div{flex:1;display:flex;align-items:center;justify-content:center}
.phase-lbl{position:absolute;top:62px;font-family:"Fira Sans",sans-serif;font-size:7px;font-weight:600;color:var(--teal-text)}
.step{position:absolute;width:110px;text-align:center}
.step .ic{width:34px;height:34px;border-radius:50%;background:var(--teal);margin:0 auto 6px;display:flex;align-items:center;justify-content:center}
.step h5{font-family:"Fira Sans",sans-serif;font-size:7px;color:var(--teal-text);margin-bottom:3px}
.step p{font-size:5.3px;line-height:1.2;color:#777}
.gantt-h{position:absolute;top:62px;font-family:"Fira Sans",sans-serif;font-weight:700;font-size:5.5px;color:var(--teal-text)}
.task{position:absolute;display:flex;align-items:center;gap:4px;font-size:4.5px;color:#555}
.task i{font-style:normal;width:9px;height:9px;background:var(--teal);color:var(--white);border-radius:2px;display:flex;align-items:center;justify-content:center;font-size:5px}
.bar{position:absolute;height:4px;background:var(--grey-bar);border-radius:2px}
.mbar{position:absolute;top:232px;height:6px;background:var(--teal);border-radius:3px}
.feat{position:absolute;left:314px;display:flex;align-items:center;gap:14px;font-size:6.8px;color:#666;line-height:1.15}
.feat span{width:20px;height:20px;border-radius:50%;background:var(--teal);display:flex;align-items:center;justify-content:center;flex:none}
.contact{display:flex;align-items:center;gap:6px;color:var(--white);font-size:7px;margin-bottom:7px}
</style>
</head>
<body>

<!-- Hero title slide -->
<div class="hero-wrap">
  <section class="slide">
    <div class="teal-bg"></div>
    <div class="art-area" role="img" aria-label="Large geometric bird artwork"></div>
    <h1 class="h-title abs" style="left:268px;top:96px">Presentation<br>Title Goes Here!</h1>
    <p class="lead abs" style="left:268px;top:164px;width:180px">Lorem ipsum dolor sit amet, consectetur adipiscing elit. Vivamus eu dui ex. Curabitur dapibus dignissim dui, in molestie metus feugiat sed.</p>
    <p class="date abs" style="left:268px;top:206px">Friday, April 21, 2023</p>
    <div class="cities">Hamburg &nbsp;|&nbsp; Wien &nbsp;|&nbsp; Berlin &nbsp;|&nbsp; München</div>
  </section>
</div>

<!-- 1 Title -->
<section class="slide" style="left:51px;top:835px">
  <div class="teal-bg"></div>
  <div class="art-area" role="img" aria-label="Large geometric bird artwork"></div>
  <h2 class="h-title abs" style="left:268px;top:100px">Presentation<br>Title Goes Here!</h2>
  <p class="lead abs" style="left:268px;top:168px;width:180px">Lorem ipsum dolor sit amet, consectetur adipiscing elit. Vivamus eu dui ex. Curabitur dapibus dignissim dui, in molestie metus feugiat sed.</p>
  <p class="date abs" style="left:268px;top:210px">Saturday, April 22, 2023</p>
  <div class="cities">Hamburg &nbsp;|&nbsp; Wien &nbsp;|&nbsp; Berlin &nbsp;|&nbsp; München</div>
</section>

<!-- 2 Brand -->
<section class="slide" style="left:609px;top:835px">
  <div class="teal-bg"></div>
  <div class="brand abs" style="left:140px;top:158px;font-size:24px"><i class="brand-dot" style="width:14px;height:14px"></i>TALVOREKSA</div>
  <div class="cities">Hamburg &nbsp;|&nbsp; Wien &nbsp;|&nbsp; Berlin &nbsp;|&nbsp; München</div>
</section>

<!-- 3 Title variant -->
<section class="slide" style="left:51px;top:1157px">
  <div class="teal-bg"></div>
  <div class="brand abs" style="left:38px;top:70px;font-size:14px"><i class="brand-dot" style="width:9px;height:9px"></i>TALVOREKSA</div>
  <h2 class="h-title abs" style="left:44px;top:118px;font-size:23px">Presentation Title<br>Goes Here!</h2>
  <p class="lead abs" style="left:44px;top:178px;width:290px">Lorem ipsum dolor sit amet, consectetur adipiscing elit. Vivamus eu dui ex. Curabitur dapibus dignissim dui, in molestie metus feugiat sed. Praesent aliquet lorem ex, eu dapibus odio varius at.</p>
  <div class="abs" style="left:44px;top:214px;border:1px solid var(--white);border-radius:4px;padding:5px 12px;color:var(--white);font-size:5.5px;font-weight:700">Saturday, April 22, 2023</div>
  <div class="cities">Hamburg &nbsp;|&nbsp; Wien &nbsp;|&nbsp; Berlin &nbsp;|&nbsp; München</div>
</section>

<!-- 4 Profile -->
<section class="slide" style="left:609px;top:1157px">
  <h3 class="name abs" style="left:30px;top:28px">Dr. Mirela<br>Hoffstaedt</h3>
  <div class="bio abs" style="left:30px;top:98px;width:255px">
    <p>Mirela knows what modern management is all about, and that from many points of view – she has not only successfully appointed many to leadership positions, but she has held those positions herself several times.</p>
    <p>As a graduate of medicine of the Nordhafen University Hospital, she first started working for Brandell Partners, where she led the healthcare academy. She was responsible for the regional healthcare sector. She was a founder and CEO of a healthcare tech start-up, which she successfully sold to an investor. And she was the CHRO of another startup that scaled very fast. To share this experience with many companies, she founded Talvoreksa Executive Search in 2021.</p>
    <p>Mirela lives in Hamburg with her family.</p>
  </div>
  <div class="photo" style="left:303px;top:0;width:210px;height:252px" role="img" aria-label="Black and white portrait photo of Dr. Mirela Hoffstaedt"></div>
  <div class="footer-brand"><i></i>Talvoreksa</div>
  <div class="footer-bar"><span>https://www.talvoreksa.io</span><span class="num">4</span></div>
</section>

<!-- 5 Profile -->
<section class="slide" style="left:51px;top:1478px">
  <h3 class="name abs" style="left:30px;top:28px">Lena Varkonyi</h3>
  <div class="bio abs" style="left:30px;top:98px;width:250px">
    <p>Lena started her career as a Global Product Manager at Aldrun in Liechtenstein before she spent 3 years in London as the European Sales Manager for Skyvane Air.</p>
    <p>She then accepted an offer from Kestrel Morrow Associates where she learned the skills of research.</p>
    <p>When her partner was transferred to Bogota in Colombia, she became self-employed (working primarily for KMA), and now, back in Vienna, she founded Talvoreksa Executive Search together with Mirela.</p>
    <p>Lena studied International Business Administration at the Danube School of Business and also graduated from the GMEP programme. She is mother of 2 children.</p>
  </div>
  <div class="photo" style="left:303px;top:0;width:210px;height:252px" role="img" aria-label="Black and white portrait photo of Lena Varkonyi"></div>
  <div class="footer-brand"><i></i>Talvoreksa</div>
  <div class="footer-bar"><span>https://www.talvoreksa.io</span><span class="num">5</span></div>
</section>

<!-- 6 Who we are -->
<section class="slide" style="left:609px;top:1478px">
  <h3 class="s-title" style="top:20px">Who We Are and How We Work</h3>
  <ul class="bullets abs" style="left:30px;top:100px;width:215px">
    <li>Longstanding experience with a passion for placing (C-Level) Executives in Healthcare and other industries</li>
    <li>In-depth expertise strong networks in healthcare and covering all relevant sub-sectors (HC Services, PE Healthcare Rollups, Elderly Care Chains, Physiotherapy, Digital Health, Medical Technology, Healthcare IT), including relevant expertise regarding the regulatory environment in Germany</li>
    <li>Expertise beyond placement and HR topics, allowing for eye-level discussion around your business</li>
    <li>Creative approaches to finding - and convincing - candidates</li>
  </ul>
  <ul class="bullets abs" style="left:284px;top:100px;width:220px">
    <li>Structured and lean digital search processes, high transparency, comprehensive candidate evaluation</li>
    <li>Referencing of candidates as part of the search process; psychometrics on demand</li>
    <li>Onboarding support to ensure a good start for the candidate</li>
    <li>We work with you personally and act as an ambassador for our clients in the market</li>
  </ul>
  <div class="footer-brand"><i></i>Talvoreksa</div>
  <div class="footer-bar"><span>https://www.talvoreksa.io</span><span class="num">6</span></div>
</section>

<!-- 7 Values -->
<section class="slide" style="left:51px;top:1800px">
  <h3 class="s-title" style="top:20px">Our Values</h3>
  <div class="abs" style="left:0;top:115px;width:540px;border-top:1px dashed #9bbac6"></div>
  <div class="values">
    <div class="value"><div class="ic"><svg width="16" height="16" viewBox="0 0 24 24"><path d="M12 21s-8-5-8-11a4.5 4.5 0 0 1 8-3 4.5 4.5 0 0 1 8 3c0 6-8 11-8 11z" fill="none" stroke="#fff" stroke-width="2"/></svg></div><h4>HONEST</h4><p>We only work with clients who can benefit from our expertise. We are not interested in status symbols, only in achieving results in a way that is transparent and beneficial for everyone.</p></div>
    <div class="value"><div class="ic"><svg width="16" height="16" viewBox="0 0 24 24"><circle cx="12" cy="8" r="4" fill="#fff"/><path d="M4 21a8 8 0 0 1 16 0z" fill="#fff"/></svg></div><h4>PERSONAL</h4><p>We put all of our resources into finding you the top talents you are looking for – and we get involved ourselves. We have excellent networks, and we are always hot on the heels of fresh talent. That is how we find the people that you need right now. And we help them realise that your company is the right place for them.</p></div>
    <div class="value"><div class="ic"><svg width="16" height="16" viewBox="0 0 24 24"><circle cx="12" cy="12" r="4" fill="none" stroke="#fff" stroke-width="2"/><path d="M12 2v4M12 18v4M2 12h4M18 12h4M5 5l3 3M16 16l3 3M5 19l3-3M16 8l3-3" stroke="#fff" stroke-width="2"/></svg></div><h4>PRAGMATIC</h4><p>We work fast. But we don't start until we have a clear goal: We begin by asking "How will you know the appointment was successful, 3 years from now?" This thought drives our process – streamlined, digital, and constantly in communication with you, from the briefing to your new staff member's first day.</p></div>
    <div class="value"><div class="ic"><svg width="16" height="16" viewBox="0 0 24 24"><circle cx="12" cy="6" r="3" fill="#fff"/><circle cx="6" cy="14" r="3" fill="#fff"/><circle cx="18" cy="14" r="3" fill="#fff"/><path d="M2 22a4 4 0 0 1 8 0zM14 22a4 4 0 0 1 8 0z" fill="#fff"/></svg></div><h4>DIVERSE</h4><p>We know where the obstacles lie, and we know where things get tough – we have worked through them ourselves, as employees, as managers, as founders, and as mothers. That's how we know how diversity really works, and how diversity can best benefit your company.</p></div>
  </div>
  <div class="footer-brand"><i></i>Talvoreksa</div>
  <div class="footer-bar"><span>https://www.talvoreksa.io</span><span class="num">7</span></div>
</section>

<!-- 8 References -->
<section class="slide" style="left:609px;top:1800px">
  <h3 class="s-title" style="top:20px">Relevant reference assignments (excerpt)</h3>
  <div class="ref" style="left:27px;top:84px"><h4>POSITION TO BE DEFINED</h4>
    <div class="row"><b>Explanation</b>Investor/Owner</div><div class="row"><b>Explanation</b>Investor/Owner</div><div class="row"><b>Explanation</b>Investor/Owner</div><div class="row"><b>Explanation</b>Investor/Owner</div><div class="row"><b>Explanation</b>Investor/Owner</div>
  </div>
  <div class="ref" style="left:282px;top:84px"><h4>POSITION TO BE DEFINED</h4>
    <div class="row"><b>Explanation</b>Investor/Owner</div><div class="row"><b>Explanation</b>Investor/Owner</div><div class="row"><b>Explanation</b>Investor/Owner</div><div class="row"><b>Explanation</b>Investor/Owner</div><div class="row"><b>Explanation</b>Investor/Owner</div>
  </div>
  <div class="footer-brand"><i></i>Talvoreksa</div>
  <div class="footer-bar"><span>https://www.talvoreksa.io</span><span class="num">8</span></div>
</section>

<!-- 9 Section break -->
<section class="slide" style="left:51px;top:2121px">
  <div class="teal-bg teal-full"></div>
  <div class="art-area" role="img" aria-label="Large geometric bird artwork"></div>
  <h2 class="h-title abs" style="left:268px;top:142px">Section Break</h2>
  <p class="lead abs" style="left:268px;top:178px;width:210px">Lorem ipsum dolor sit amet, consectetur adipiscing elit. Vivamus eu dui ex. Curabitur dapibus dignissim dui, in molestie metus feugiat sed.</p>
</section>

<!-- 10 Search process -->
<section class="slide" style="left:609px;top:2121px">
  <h3 class="s-title" style="top:20px">Search Process</h3>
  <span class="phase-lbl" style="left:97px">Phase 1</span>
  <span class="phase-lbl" style="left:263px">Phase 2</span>
  <span class="phase-lbl" style="left:428px">Phase 3</span>
  <div class="proc-band"><div>Research - Longlist</div><div>Focus &amp; Interviews - Shortlist</div><div>Completion</div></div>
  <div class="abs" style="left:0;top:108px;width:540px;border-top:1px dashed #9bbac6"></div>
  <span class="abs" style="left:20px;top:113px;font-size:5px;color:var(--teal-text)">CW 1</span>
  <span class="abs" style="left:504px;top:113px;font-size:5px;color:var(--teal-text)">CW 2</span>
  <div class="step" style="left:4px;top:128px"><div class="ic"><svg width="14" height="14" viewBox="0 0 24 24"><rect x="4" y="4" width="16" height="16" rx="3" fill="#fff"/></svg></div><h5>Kickoff</h5><p>Discuss and agree on profile, position specification and target list.</p></div>
  <div class="step" style="left:110px;top:162px"><div class="ic"><svg width="14" height="14" viewBox="0 0 24 24"><circle cx="10" cy="10" r="6" fill="none" stroke="#fff" stroke-width="3"/><path d="M15 15l6 6" stroke="#fff" stroke-width="3"/></svg></div><h5>Research</h5><p>Active and passive research, approach of potential candidates</p></div>
  <div class="step" style="left:215px;top:128px"><div class="ic"><svg width="14" height="14" viewBox="0 0 24 24"><circle cx="9" cy="8" r="4" fill="#fff"/><path d="M2 21a7 7 0 0 1 14 0z" fill="#fff"/><rect x="15" y="3" width="7" height="6" rx="1" fill="#fff"/></svg></div><h5>Interviews</h5><p>Presentation of prioritised profiles, client interviews</p></div>
  <div class="step" style="left:320px;top:162px"><div class="ic"><svg width="14" height="14" viewBox="0 0 24 24"><circle cx="12" cy="7" r="3" fill="#fff"/><circle cx="5" cy="10" r="3" fill="#fff"/><circle cx="19" cy="10" r="3" fill="#fff"/><path d="M1 20a4 4 0 0 1 22 0z" fill="#fff"/></svg></div><h5>References</h5><p>Assessments (optional), taking references</p></div>
  <div class="step" style="left:425px;top:128px"><div class="ic"><svg width="14" height="14" viewBox="0 0 24 24"><circle cx="12" cy="8" r="4" fill="#fff"/><path d="M4 21a8 8 0 0 1 16 0z" fill="#fff"/></svg></div><h5>Selection final candidate</h5><p>Contract negotiation and onboarding, feedback discussion</p></div>
  <div class="footer-brand"><i></i>Talvoreksa</div>
  <div class="footer-bar"><span>https://www.talvoreksa.io</span><span class="num">10</span></div>
</section>

<!-- 11 Timeline -->
<section class="slide" style="left:51px;top:2442px">
  <h3 class="s-title" style="top:20px">Draft Project Timeline for placement</h3>
  <span class="gantt-h" style="left:50px">Phase 1: Open the search &amp; screen -LONGLIST</span>
  <span class="gantt-h" style="left:236px">Phase 2: Narrow the focus - SHORTLIST</span>
  <span class="gantt-h" style="left:409px">Phase 3: Close the search</span>
  <div class="abs" style="left:36px;top:90px;height:130px;border-left:1px dashed #bbb"></div>
  <div class="abs" style="left:222px;top:90px;height:130px;border-left:1px dashed #bbb"></div>
  <div class="abs" style="left:395px;top:90px;height:130px;border-left:1px dashed #bbb"></div>
  <div class="task" style="left:112px;top:97px"><i>4</i>Approach potential candidates</div><div class="bar" style="left:112px;top:110px;width:175px"></div>
  <div class="task" style="left:90px;top:118px"><i>3</i>Source &amp; screen the market</div><div class="bar" style="left:90px;top:131px;width:120px"></div>
  <div class="task" style="left:33px;top:148px"><i>2</i>Define the target universe</div><div class="bar" style="left:33px;top:161px;width:80px"></div>
  <div class="task" style="left:148px;top:148px"><i>6</i>Present candidates &amp; client interviews; first referencing</div><div class="bar" style="left:148px;top:161px;width:185px"></div>
  <div class="task" style="left:13px;top:178px"><i>1</i>Kick-Off: agree on profile and spec</div><div class="bar" style="left:13px;top:191px;width:45px"></div>
  <div class="task" style="left:130px;top:178px"><i>5</i>Client interviews</div><div class="bar" style="left:130px;top:191px;width:70px"></div>
  <div class="task" style="left:385px;top:97px">Select the final candidate</div>
  <div class="task" style="left:395px;top:118px"><i>7</i>Negotiate contract &amp; begin onboarding</div><div class="bar" style="left:395px;top:131px;width:60px"></div>
  <div class="task" style="left:405px;top:148px"><i>8</i>360-degree referencing</div><div class="bar" style="left:405px;top:161px;width:40px"></div>
  <div class="task" style="left:460px;top:178px"><i>9</i>Collect feedback from client</div><div class="bar" style="left:460px;top:191px;width:40px"></div>
  <div class="abs" style="left:10px;top:210px;width:520px;border-top:1px solid #888"></div>
  <div class="abs" style="left:10px;top:213px;width:520px;display:flex;justify-content:space-between;font-size:4.5px;color:#555"><span>W</span><span>12</span><span>13</span><span>14</span><span>15</span><span>16</span><span>17</span><span>18</span><span>19</span><span>20</span><span>21</span><span>22</span><span>23</span><span>24</span><span>25</span><span>26</span><span>27</span><span>W</span></div>
  <div class="mbar" style="left:40px;width:102px"></div><div class="mbar" style="left:150px;width:108px"></div><div class="mbar" style="left:266px;width:108px"></div><div class="mbar" style="left:382px;width:108px"></div>
  <div class="abs" style="left:0;top:244px;width:540px;font-size:4.5px;color:var(--teal-text)"><span class="abs" style="left:28px">03/2023</span><span class="abs" style="left:145px">04/2023</span><span class="abs" style="left:262px">05/2023</span><span class="abs" style="left:378px">06/2023</span></div>
  <div class="footer-brand"><i></i>Talvoreksa</div>
  <div class="footer-bar"><span>https://www.talvoreksa.io</span><span class="num">11</span></div>
</section>

<!-- 12 Digital tool -->
<section class="slide" style="left:609px;top:2442px">
  <div class="abs" style="left:26px;top:28px;width:268px;height:172px;border-radius:9px;background:#1b1b1b;padding:6px">
    <div style="width:100%;height:100%;border-radius:4px;background:linear-gradient(180deg,#f4f7f9,#e4ebef)" role="img" aria-label="Screen of the online candidate dashboard"></div>
  </div>
  <h3 class="name abs" style="left:314px;top:34px;font-size:18px">Digital Tool for<br>Full Transparency</h3>
  <div class="feat" style="top:100px"><span><svg width="11" height="11" viewBox="0 0 24 24"><circle cx="12" cy="12" r="9" fill="none" stroke="#fff" stroke-width="2.5"/><path d="M12 7v5l3 3" stroke="#fff" stroke-width="2.5" fill="none"/></svg></span>Follow the progress of the project<br>24/7 real-time</div>
  <div class="feat" style="top:132px"><span><svg width="11" height="11" viewBox="0 0 24 24"><path d="M4 6h16M4 12h16M4 18h16" stroke="#fff" stroke-width="2.5"/></svg></span>Prioritize and evaluate candidates<br>and provide feedback</div>
  <div class="feat" style="top:164px"><span><svg width="11" height="11" viewBox="0 0 24 24"><rect x="5" y="3" width="14" height="18" rx="2" fill="none" stroke="#fff" stroke-width="2.5"/></svg></span>You can view the list of<br>target companies at any time</div>
  <div class="feat" style="top:196px"><span><svg width="11" height="11" viewBox="0 0 24 24"><rect x="7" y="2" width="10" height="20" rx="2" fill="none" stroke="#fff" stroke-width="2.5"/></svg></span>Access to the relevant information on<br>all candidates at all times</div>
  <div class="footer-brand"><i></i>Talvoreksa</div>
  <div class="footer-bar"><span>https://www.talvoreksa.io</span><span class="num">12</span></div>
</section>

<!-- 13 Thank you -->
<section class="slide" style="left:330px;top:2764px">
  <div class="teal-bg"></div>
  <div class="art-area" role="img" aria-label="Large geometric bird artwork"></div>
  <h2 class="h-title abs" style="left:282px;top:110px">Thank you!</h2>
  <div class="abs" style="left:282px;top:168px">
    <p style="color:var(--white);font-size:8px;font-weight:600;margin-bottom:12px">Contact Us</p>
    <div class="contact"><svg width="8" height="8" viewBox="0 0 24 24"><path d="M5 3h4l2 5-3 2a12 12 0 0 0 6 6l2-3 5 2v4a2 2 0 0 1-2 2A18 18 0 0 1 3 5a2 2 0 0 1 2-2z" fill="#fff"/></svg>Phone Number Goes Here</div>
    <div class="contact"><svg width="8" height="8" viewBox="0 0 24 24"><circle cx="12" cy="12" r="9" fill="none" stroke="#fff" stroke-width="2.5"/><circle cx="12" cy="12" r="3.5" fill="none" stroke="#fff" stroke-width="2.5"/></svg>E-Mail Address Goes Here</div>
    <div class="contact"><svg width="8" height="8" viewBox="0 0 24 24"><circle cx="12" cy="12" r="9" fill="none" stroke="#fff" stroke-width="2"/><path d="M3 12h18M12 3c4 4 4 14 0 18M12 3c-4 4-4 14 0 18" stroke="#fff" stroke-width="2" fill="none"/></svg>URL Address Goes Here</div>
  </div>
  <div class="cities">Hamburg &nbsp;|&nbsp; Wien &nbsp;|&nbsp; Berlin &nbsp;|&nbsp; München</div>
</section>

</body>
</html>
```